Engineering Consultant Business Card

I'm starting a new business as a high-end engineering consultant in a niche field. I've attached the jpg for my logo plus the branding guideline document that I've been following. You can see my business website here: www.tarvikworks.com
I'd like a business card that has the logo on one side, then the other side has (in any order): Tarvik Works, Inc.
Dana Whitlock
President and Chief EMC Engineer
www.tarvikworks.com
dana@tarvikworks.com
Optional: motto "We will solve your EMC problems as early as possible—ideally before they even start."
I'm not planning on including a phone number
Target Market(s)
Businesses, especially makers of electronics hardware
Industry/Entity Type
Electrical engineering
Contact Information for Business Card
Company name, my name, website, email

```html
<!DOCTYPE html>
<html lang="en">
<head>
<meta charset="UTF-8">
<title>Tarvik Works, Inc. — Business Card</title>
<link href="https://fonts.googleapis.com/css2?family=Montserrat:wght@400;500;700&display=swap" rel="stylesheet">
<style>
  :root {
    --page-bg: #e4e5e8;
    --brand-blue: #27469a;
    --brand-blue-deep: #22418f;
    --brand-blue-light: #7189c1;
    --band-white: #f1f1f1;
    --paper-white: #ffffff;
    --icon-cut: #3d5aa3;
    --card-radius: 22px;
  }
  * { box-sizing: border-box; margin: 0; padding: 0; }
  html, body {
    width: 1200px; height: 1200px; overflow: hidden;
    background: var(--page-bg);
    font-family: "Montserrat", sans-serif;
  }
  .stage {
    position: relative; width: 1200px; height: 1200px;
    display: flex; flex-direction: column; align-items: center; justify-content: center; gap: 64px;
  }
  .card {
    position: relative; width: 760px; height: 434px;
    border-radius: var(--card-radius); overflow: hidden;
    box-shadow: 0 14px 30px rgba(0,0,0,0.18);
  }

  /* Front */
  .card--front {
    background: linear-gradient(90deg, var(--brand-blue-light) 0%, #4f6ab0 35%, var(--brand-blue) 70%, var(--brand-blue) 100%);
  }
  .front-mark {
    position: absolute; left: 0; right: 0; top: 120px;
    display: flex; align-items: center; justify-content: center; gap: 22px;
  }
  .front-mark__dot {
    width: 70px; height: 70px; border-radius: 50%;
    border: 12px solid var(--paper-white);
  }
  .front-mark__name {
    color: var(--paper-white); font-weight: 700; font-size: 68px; letter-spacing: 1px;
  }
  .front-tab {
    position: absolute; bottom: 0; left: 50%; transform: translateX(-50%);
    width: 330px; height: 82px;
    background: var(--paper-white);
    border-radius: 34px 34px 0 0;
    display: flex; align-items: center; justify-content: center;
  }
  .front-tab__company {
    color: var(--brand-blue); font-weight: 500; font-size: 17px; letter-spacing: 0.5px;
  }

  /* Back */
  .card--back {
    background: linear-gradient(90deg, #6b84bd 0%, #3d5aa3 35%, var(--brand-blue-deep) 70%, var(--brand-blue) 100%);
  }
  .back-band {
    position: absolute; left: 0; right: 0; top: 160px; height: 160px;
    background: var(--band-white);
  }
  .back-head {
    position: absolute; left: 0; right: 0; top: 44px; text-align: center; color: var(--paper-white);
  }
  .back-head__name { font-weight: 700; font-size: 34px; letter-spacing: 1px; }
  .back-head__title { font-weight: 500; font-size: 18px; letter-spacing: 0.8px; margin-top: 8px; }
  .back-mark {
    position: absolute; left: 0; right: 0; top: 160px; height: 160px;
    display: flex; align-items: center; justify-content: center; gap: 14px;
  }
  .back-mark__dot {
    width: 42px; height: 42px; border-radius: 50%;
    border: 7px solid var(--brand-blue);
  }
  .back-mark__name { color: var(--brand-blue); font-weight: 700; font-size: 38px; letter-spacing: 0.5px; }

  .contact-list {
    position: absolute; left: 64px; top: 348px; list-style: none; color: var(--paper-white);
  }
  .contact-list__item {
    display: flex; align-items: center; gap: 14px;
    font-size: 18px; font-weight: 500; letter-spacing: 0.4px; line-height: 28px;
  }
  .contact-list__icon { width: 16px; height: 16px; flex: none; }
  .address {
    position: absolute; right: 56px; top: 348px; text-align: right;
    color: var(--paper-white); font-size: 18px; font-weight: 500; letter-spacing: 0.4px; line-height: 28px;
    font-style: normal;
  }
</style>
</head>
<body>
<main class="stage">

  <section class="card card--front" aria-label="Business card front">
    <div class="front-mark">
      <span class="front-mark__dot"></span>
      <span class="front-mark__name">Tarvik Works</span>
    </div>
    <div class="front-tab">
      <span class="front-tab__company">Tarvik Works, Inc.</span>
    </div>
  </section>

  <section class="card card--back" aria-label="Business card back">
    <div class="back-band"></div>
    <header class="back-head">
      <h1 class="back-head__name">Dana Whitlock</h1>
      <p class="back-head__title">President and chief EMC Engineer</p>
    </header>
    <div class="back-mark">
      <span class="back-mark__dot"></span>
      <span class="back-mark__name">Tarvik Works</span>
    </div>

    <ul class="contact-list">
      <li class="contact-list__item">
        <svg class="contact-list__icon" viewBox="0 0 16 16" fill="#fff" aria-hidden="true">
          <path d="M1 3.5h14v9H1z M1 3.5l7 5 7-5" stroke="var(--icon-cut)" stroke-width="1.2"/>
        </svg>
        dana@tarvikworks.com
      </li>
      <li class="contact-list__item">
        <svg class="contact-list__icon" viewBox="0 0 16 16" fill="none" stroke="#fff" stroke-width="1.6" aria-hidden="true">
          <circle cx="8" cy="8" r="6.5"/><ellipse cx="8" cy="8" rx="2.8" ry="6.5"/><path d="M1.5 8h13"/>
        </svg>
        www.tarvikworks.com
      </li>
    </ul>

    <address class="address">
      418 Alder Crest Lane<br>
      Brookhaven Maine 04512
    </address>
  </section>

</main>
</body>
</html>
```